Business card design needed

We need a business card for a new business. We are called Tiny Toilers Gear, and we make replica kid size clothing, mainly hi vis shirts, work trousers and shorts. Our long term goal is to include clothing for numerous trades and professions, for our littlest Aussies. We would like a kid friendly card using navy blue, bright orange, bright yellow and bright pink. We haven't set up our web page yet because we want to base it on our final business card design.
Updates

Industry/Entity Type

Clothing

```html
<!DOCTYPE html>
<html lang="en">
<head>
<meta charset="utf-8">
<title>Tiny Toilers Gear – Business Card</title>
<link rel="stylesheet" href="https://fonts.googleapis.com/css2?family=Fredoka:wght@600&family=Poppins:wght@600&display=swap">
<style>
  :root {
    --navy: #23206e;
    --navy-deep: #1a1856;
    --pink: #ec1c8c;
    --orange: #f7941d;
    --yellow: #ffe000;
    --white: #ffffff;
    --stage: #ececec;
    --card-shadow: rgba(0, 0, 0, 0.18);
  }
  * { margin: 0; padding: 0; box-sizing: border-box; }
  html, body { width: 1200px; height: 634px; overflow: hidden; }
  body {
    background: var(--stage);
    position: relative;
    font-family: "Poppins", sans-serif;
  }
  .card {
    position: absolute;
    top: 168px;
    width: 520px;
    height: 297px;
    overflow: hidden;
    box-shadow: 0 6px 18px var(--card-shadow);
  }
  .card--front { left: 60px; background: var(--white); }
  .card--back { left: 620px; background: var(--navy); }
  .card__art { position: absolute; inset: 0; width: 100%; height: 100%; }
  .brand-name {
    position: absolute;
    font-family: "Fredoka", sans-serif;
    font-weight: 600;
    color: var(--pink);
    line-height: 1;
    letter-spacing: 0.5px;
  }
  .card--front .brand-name { left: 22px; top: 24px; font-size: 34px; width: 200px; }
  .card--back .brand-name { left: 118px; top: 138px; font-size: 36px; width: 240px; }
  .web-address {
    position: absolute;
    font-size: 10px;
    font-weight: 600;
    color: var(--white);
    letter-spacing: 0.2px;
  }
  .card--front .web-address { left: 30px; bottom: 14px; }
  .card--back .web-address { left: 200px; bottom: 40px; }
  .web-address::before {
    content: "";
    display: inline-block;
    width: 7px; height: 7px;
    border-radius: 50%;
    background: var(--white);
    margin-right: 8px;
    vertical-align: middle;
  }
</style>
</head>
<body>

<section class="card card--front" aria-label="Business card front">
  <svg class="card__art" viewBox="0 0 520 297" aria-hidden="true">
    <polygon points="0,150 520,118 520,132 0,172" fill="var(--pink)"/>
    <polygon points="0,172 520,132 520,144 0,182" fill="var(--yellow)"/>
    <polygon points="0,182 520,144 520,154 0,190" fill="var(--orange)"/>
    <polygon points="0,190 520,154 520,164 0,198" fill="var(--pink)"/>
    <path d="M0,198 L520,164 L520,297 L0,297 Z" fill="var(--navy)"/>
  </svg>
  <svg class="card__art" viewBox="0 0 520 297" role="img" aria-label="Illustration of three children in work clothes dancing to music">
    <defs>
      <linearGradient id="kidsTone" x1="0" y1="0" x2="1" y2="1">
        <stop offset="0" stop-color="#f6a9cf" stop-opacity="0.75"/>
        <stop offset="1" stop-color="#f9c27a" stop-opacity="0.75"/>
      </linearGradient>
    </defs>
    <rect x="250" y="30" width="250" height="215" rx="24" fill="url(#kidsTone)"/>
  </svg>
  <p class="brand-name">Tiny Toilers Gear</p>
  <p class="web-address">www.tinytoilersgear.com</p>
</section>

<section class="card card--back" aria-label="Business card back">
  <svg class="card__art" viewBox="0 0 520 297" aria-hidden="true">
    <path d="M60,297 C28,250 34,178 92,166 C80,104 150,66 206,90 C240,36 330,36 362,92 C420,70 486,116 468,170 C522,186 520,262 470,280 L470,297"
          fill="none" stroke="var(--white)" stroke-width="8" stroke-linejoin="round"/>
  </svg>
  <p class="brand-name">Tiny Toilers Gear</p>
  <p class="web-address">www.tinytoilersgear.com</p>
</section>

</body>
</html>
```